Recruitment #1

We are looking for an effective ad to recruit work from home Loan Officers for our Mortgage Brokerage.
Use the following text...
Earn Mortgage Income in your sleep. Its as easy as 1, 2, 3.....
1) Solicit Potential Applicants (Word of Mouth, Email, Social Media etc.)
2) Take Complete Applications & Submit Them
3) Wait to Get Paid.......(Avg. $2,500 per closing)
"You open the Bluegate, We'll handle the rest"
No Experience Necessary
No Goals or Quotas
No Office Hours / Work from Home Office
...and We Fully Reimburse ALL LICENSING FEES!!
Email Resume to mkowal@bluegatehomeloans.com
Bluegate Financial Services, Inc.
731 W Orchard Avenue, #318
Baltimore, MD 21417
NMLS #386147
www.bluegatehomeloans.com
Phone (800) 640-2915
Licensed Mortgage Broker in MD and DC since 1997
Professionals looking to earn part time income at Loan Officers, preferably with strong social media following.
Loan

```html
<!DOCTYPE html>
<html lang="en">
<head>
<meta charset="utf-8">
<title>Bluegate Financial Services – Loan Officer Recruitment</title>
<link href="https://fonts.googleapis.com/css2?family=Bebas+Neue&family=Quicksand:wght@500;600&family=Open+Sans:wght@600;700&display=swap" rel="stylesheet">
<style>
  :root {
    --mat: #cbcbcb;
    --paper: #ffffff;
    --sky-deep: #2f6a9e;
    --band: #6fa3cc;
    --ink: #2b2b2b;
    --ink-soft: #555555;
    --rule: #c9c9c9;
    --arrow: #5b9bd5;
    --badge: #2f5fa8;
  }
  * { margin: 0; padding: 0; box-sizing: border-box; }
  html, body { width: 923px; height: 1200px; overflow: hidden; background: var(--mat); }
  .flyer {
    position: absolute; left: 126px; top: 130px; width: 670px; height: 941px;
    background: linear-gradient(160deg, #ffffff 0%, #f1f3f5 60%, #ffffff 100%);
    overflow: hidden; font-family: "Quicksand", sans-serif; color: var(--ink);
  }
  .hero { position: absolute; left: 0; top: 0; width: 670px; height: 460px; }
  .logo {
    position: absolute; left: 484px; top: 32px; width: 136px; height: 88px;
    background: var(--paper); border-radius: 50%;
    display: flex; align-items: center; justify-content: center; gap: 6px; padding: 0 12px;
    font-weight: 600; font-size: 11px; line-height: 1.2; color: var(--sky-deep); text-align: center;
  }
  .logo .dot { width: 12px; height: 12px; border-radius: 50%; background: var(--sky-deep); flex: none; }
  .condensed {
    position: absolute; text-align: center; white-space: nowrap;
    font-family: "Bebas Neue", sans-serif; font-weight: 400;
    transform: scaleX(0.68); transform-origin: center top;
  }
  .headline { left: 222px; top: 160px; width: 500px; color: #fff; font-size: 68px; line-height: 76px; }
  .slogan { left: 286px; top: 494px; width: 400px; color: var(--ink-soft); font-size: 38px; line-height: 40px; }
  .step-num {
    position: absolute; left: 172px; width: 28px; height: 28px; border-radius: 4px; background: var(--arrow);
    color: #fff; font-family: "Open Sans", sans-serif; font-weight: 700; font-size: 19px; line-height: 28px; text-align: center;
  }
  .step-text { position: absolute; left: 37px; width: 272px; text-align: center; white-space: nowrap; }
  .step-title { font-size: 19.5px; font-weight: 500; line-height: 25px; }
  .step-note { font-size: 12.5px; font-weight: 500; line-height: 16px; }
  .divider { position: absolute; left: 37px; width: 272px; height: 1px; background: var(--rule); }
  .perks { position: absolute; left: 342px; top: 603px; list-style: none; }
  .perks li {
    position: relative; padding-left: 29px; font-size: 19px; font-weight: 500; line-height: 24px;
    color: var(--ink-soft); margin-bottom: 7px; letter-spacing: 0.3px; white-space: nowrap;
  }
  .perks svg { position: absolute; left: 0; top: 4px; }
  .reimburse {
    position: absolute; left: 0; top: 765px; width: 670px; text-align: center;
    font-size: 21px; font-weight: 500; color: var(--ink-soft); letter-spacing: 0.3px;
  }
  .footer-rule { position: absolute; left: 0; top: 801px; width: 670px; height: 1px; background: #e2e2e2; }
  .contact {
    position: absolute; font-style: normal; white-space: nowrap;
    font-family: "Open Sans", sans-serif; font-weight: 600; font-size: 12.5px; line-height: 19.5px; color: #222;
  }
  .contact.office { left: 38px; top: 804px; }
  .contact.web { left: 187px; top: 823.5px; width: 300px; text-align: center; }
  .social {
    position: absolute; left: 486px; top: 814px; width: 144px; height: 46px;
    border: 1.5px solid var(--badge); border-radius: 3px; background: #fff;
    display: flex; align-items: center; justify-content: center; gap: 7px; white-space: nowrap;
    font-family: "Open Sans", sans-serif; font-weight: 700; font-size: 12.5px; color: var(--badge);
  }
  .social .square { width: 16px; height: 16px; background: var(--badge); flex: none; }
  .band {
    position: absolute; left: 0; top: 886px; width: 670px; height: 55px; background: var(--band);
    color: #fff; font-family: "Open Sans", sans-serif; font-weight: 700; font-size: 17.5px;
    text-align: center; padding-top: 4px;
  }
</style>
</head>
<body>
<main class="flyer">
  <svg class="hero" viewBox="0 0 670 460" role="img" aria-label="Photo of a smiling businessman in a suit with folded arms, standing in a bright glass-walled office">
    <defs>
      <linearGradient id="office" x1="0" y1="0" x2="1" y2="1">
        <stop offset="0" stop-color="#9ccbee"/>
        <stop offset="0.5" stop-color="#5d9bcf"/>
        <stop offset="1" stop-color="#3f7fb6"/>
      </linearGradient>
      <linearGradient id="figure" x1="0" y1="0" x2="0" y2="1">
        <stop offset="0" stop-color="#3b5670" stop-opacity="0.35"/>
        <stop offset="1" stop-color="#1e2c3a" stop-opacity="0.6"/>
      </linearGradient>
    </defs>
    <polygon points="0,0 670,0 670,458 0,388" fill="url(#office)"/>
    <polygon points="60,400 80,230 150,200 270,200 310,240 300,435" fill="url(#figure)"/>
  </svg>

  <div class="logo"><span class="dot"></span><span>Bluegate Financial Services, Inc.</span></div>

  <h1 class="condensed headline">Earn Mortgage Income<br>in your sleep.<br>Its as easy as 1, 2, 3...</h1>

  <section class="steps">
    <span class="step-num" style="top:443px">1</span>
    <div class="step-text" style="top:474px">
      <p class="step-title">Solicit Potential Applicants</p>
      <p class="step-note">(Word of Mouth, Email, Social Media etc.)</p>
    </div>
    <div class="divider" style="top:532px"></div>
    <span class="step-num" style="top:539px">2</span>
    <div class="step-text" style="top:570px">
      <p class="step-title">Take Complete Applications<br>&amp; Submit Them</p>
    </div>
    <div class="divider" style="top:630px"></div>
    <span class="step-num" style="top:639px">3</span>
    <div class="step-text" style="top:670px">
      <p class="step-title">Wait to Get Paid...</p>
      <p class="step-note">(Avg. $2,500 per closing)</p>
    </div>
  </section>

  <h2 class="condensed slogan">You open the Bluegate,<br>We'll handle the rest</h2>

  <ul class="perks">
    <li><svg width="24" height="16" viewBox="0 0 24 16"><path d="M0,5 H14 V0 L24,8 L14,16 V11 H0 Z" fill="var(--arrow)"/></svg>No Experience Necessary</li>
    <li><svg width="24" height="16" viewBox="0 0 24 16"><path d="M0,5 H14 V0 L24,8 L14,16 V11 H0 Z" fill="var(--arrow)"/></svg>No Goals or Quotas</li>
    <li><svg width="24" height="16" viewBox="0 0 24 16"><path d="M0,5 H14 V0 L24,8 L14,16 V11 H0 Z" fill="var(--arrow)"/></svg>No Office Hours / Work<br>from Home Office</li>
  </ul>

  <p class="reimburse">...and We Fully Reimburse ALL LICENSING FEES!</p>

  <div class="footer-rule"></div>
  <address class="contact office">
    Bluegate Financial Services, Inc.<br>
    731 W Orchard Avenue, #318<br>
    Baltimore, MD 21417<br>
    NMLS #386147
  </address>
  <address class="contact web">
    www.bluegatehomeloans.com<br>
    Phone (800) 640-2915<br>
    Email resume to mkowal@bluegatehomeloans.com
  </address>

  <div class="social"><span class="square"></span><span>Like us on Hearthly</span></div>

  <footer class="band">Licensed Mortgage Broker in MD and DC since 1997</footer>
</main>
</body>
</html>
```